Design a web site for my business - Brellan Coatworks Mackaby.

We are a family business that handles design, fabrication and installation of powder coated aluminum, stainless steel and glass products. Including handrails, privacy slat screens, electric gates and pool fencing. We are based in the Whitsundays in North Queensland and service an area from Airlie Beach to Townsville.

Target Market(s)

Domestic and commercial

Industry/Entity Type

fabrication - manufacturing

Coding

Coded - Design and coding required

Number of Pages Required

5+ page

Colors
0054AA
0677BA
7BADD7
CADEEF
E8F1F8

Requirements
Must have
• photo galleries, contact page, one page for privacy screens, balustrades, glass fencing, stainless steel handrail, powder coated aluminium handrails and pool fencing

```html
<!DOCTYPE html>
<html lang="en">
<head>
<meta charset="utf-8">
<title>Brellan Coatworks Mackaby</title>
<link href="https://fonts.googleapis.com/css2?family=Poppins:wght@400;500;600;700&display=swap" rel="stylesheet">
<style>
:root{
  --blue:#2166bb;
  --blue-dark:#0054aa;
  --ink:#1f2328;
  --text:#444b52;
  --nav:#3a3f45;
  --band:#3e4246;
  --footer:#1f1f1f;
  --soft:#f4f4f4;
  --card:#e8eef7;
  --white:#ffffff;
  --star:#f08a00;
}
*{box-sizing:border-box;margin:0;padding:0}
html,body{width:1200px;height:3770px;overflow:hidden}
body{position:relative;font-family:'Poppins',sans-serif;color:var(--ink);background:var(--white)}
.abs{position:absolute}
a{color:inherit;text-decoration:none}
.btn{position:absolute;background:var(--blue);color:var(--white);font-size:12px;font-weight:500;display:flex;align-items:center;justify-content:center;text-transform:uppercase;letter-spacing:.2px}
.brand{font-weight:600;color:var(--blue-dark);white-space:nowrap}
.top-contact{position:absolute;display:flex;align-items:center;gap:10px;top:26px}
.top-contact .ic{width:32px;height:32px;border:1.5px solid #c9d3de;border-radius:50%;display:flex;align-items:center;justify-content:center}
.top-contact small{display:block;font-size:11px;color:var(--text);line-height:1.2}
.top-contact b{font-size:14px;font-weight:500;line-height:1.3;white-space:nowrap}
.social-dot{position:absolute;width:14px;height:14px;border-radius:50%;background:var(--blue)}
.nav{top:89px;left:0;width:1200px;height:45px;background:var(--nav)}
.nav a{position:absolute;top:0;height:45px;line-height:45px;color:var(--white);font-size:13px;transform:translateX(-50%)}
.nav a.active{font-weight:600}
.nav a.btn{transform:none}
.nav .underline{position:absolute;left:154px;top:42px;width:52px;height:2px;background:var(--white)}
.hero{top:134px;left:0;width:1200px;height:456px;background:linear-gradient(100deg,#2c2a28 0%,#4a4844 30%,#8a8580 55%,#b9a58b 72%,#6f6a66 100%)}
.hero-title{left:160px;top:254px;font-size:49px;line-height:56px;font-weight:600;color:var(--white)}
.hero-sub{left:161px;top:376px;width:460px;font-size:14px;line-height:16px;color:var(--white)}
.about-bg{top:590px;left:0;width:1200px;height:486px;background:var(--soft)}
.photo{position:absolute}
h2{font-weight:600;color:var(--ink)}
.about-title{left:650px;top:691px;font-size:30px}
.about-sub{left:650px;top:734px;font-size:16px;font-weight:500}
.about-text{left:650px;top:770px;width:392px;font-size:11.5px;line-height:16.5px;color:var(--text)}
.center{left:0;width:1200px;text-align:center}
.sec-title{font-size:30px}
.sec-sub{font-size:16px;font-weight:500}
.sec-text{font-size:12px;line-height:16px;color:var(--text)}
.svc-box{position:absolute;width:379px;height:214px;background:var(--blue);color:var(--white);padding:36px 34px 0;box-shadow:0 6px 18px rgba(0,0,0,.15)}
.svc-box.dark{background:var(--nav)}
.svc-box h3{font-size:20px;font-weight:500;margin-bottom:12px}
.svc-box p{font-size:13px;line-height:19.5px;margin-bottom:10px}
.svc-box .more{font-size:13px;display:flex;align-items:center;gap:8px}
.band{top:2352px;left:0;width:1200px;height:171px;background:var(--band)}
.feat{position:absolute;width:240px;text-align:center;color:var(--white);transform:translateX(-50%)}
.feat svg{display:block;margin:0 auto}
.feat h4{font-size:15px;font-weight:500;margin-top:10px}
.feat p{font-size:11.5px;color:#d6d9dc}
.tcard{position:absolute;top:3157px;height:204px;background:var(--card)}
.tcard .avatar{position:absolute;left:26px;top:22px;width:66px;height:66px;border-radius:50%;background:linear-gradient(135deg,#8d7a6a,#3f4a5a)}
.tcard .name{position:absolute;left:107px;top:38px;font-size:14px;font-weight:500}
.tcard .stars{position:absolute;left:107px;top:57px;color:var(--star);font-size:13px;letter-spacing:1px}
.tcard p{position:absolute;left:26px;top:112px;width:232px;font-size:11.5px;line-height:18px;color:var(--text)}
.dots{top:3385px;left:567px;display:flex;gap:8px}
.dots span{width:6px;height:6px;border-radius:50%;background:#b9c6d6}
.dots span:first-child{background:var(--blue)}
.footer{top:3452px;left:0;width:1200px;height:318px;background:var(--footer);color:var(--white)}
.fcol{position:absolute;top:3499px;font-size:12px;color:var(--white)}
.fcol h5{font-size:13px;font-weight:500;margin-bottom:12px;color:var(--white)}
.fcol li{list-style:none;height:30px;color:#e2e2e2}
.fcontact{position:absolute;left:826px;font-size:12px;display:flex;align-items:center;gap:12px;color:#e2e2e2}
.copy{top:3705px;font-size:12px;color:#e2e2e2}
.legal{top:3730px;font-size:12px;color:var(--blue)}
</style>
</head>
<body>

<!-- Header -->
<div class="abs brand" style="left:161px;top:24px;font-size:24px">Brellan Coatworks Mackaby</div>
<div class="top-contact" style="left:542px">
  <span class="ic"><svg width="14" height="14" viewBox="0 0 24 24"><path d="M6.6 10.8a15 15 0 0 0 6.6 6.6l2.2-2.2a1 1 0 0 1 1-.25 11 11 0 0 0 3.6.6 1 1 0 0 1 1 1V20a1 1 0 0 1-1 1A17 17 0 0 1 3 4a1 1 0 0 1 1-1h3.5a1 1 0 0 1 1 1 11 11 0 0 0 .6 3.6 1 1 0 0 1-.25 1z" fill="var(--blue)"/></svg></span>
  <div><small>Call Us</small><b>+61 7 5550 1234</b></div>
</div>
<div class="top-contact" style="left:730px">
  <span class="ic"><svg width="14" height="12" viewBox="0 0 24 18"><rect x="1" y="1" width="22" height="16" rx="2" fill="var(--blue)"/><path d="M2 3l10 7 10-7" stroke="#fff" stroke-width="1.6" fill="none"/></svg></span>
  <div><small>Email</small><b>info@brellancoatworks.com</b></div>
</div>
<span class="social-dot" style="left:994px;top:37px"></span>
<span class="social-dot" style="left:1024px;top:37px"></span>

<!-- Navigation -->
<nav class="abs nav">
  <a class="active" style="left:180px">HOME</a>
  <a style="left:312px">ABOUT US</a>
  <a style="left:473px">SERVICES</a>
  <a style="left:624px">PROJECTS</a>
  <a style="left:785px">CONTACT</a>
  <span class="underline"></span>
  <a class="btn" style="left:854px;width:185px;height:45px;font-size:13px">REQUEST A QUOTE</a>
</nav>

<!-- Hero -->
<section>
  <div class="abs hero" role="img" aria-label="Glass and stainless steel balustrade on a terrace overlooking the water at sunset"></div>
  <h1 class="abs hero-title">Premium Aluminium<br>Glass &amp; Steel Solutions</h1>
  <p class="abs hero-sub">Custom design, fabrication and installation for residential &amp; commercial properties.</p>
  <a class="btn" style="left:161px;top:424px;width:138px;height:37px">Learn More</a>
  <svg class="abs" style="left:13px;top:353px" width="12" height="18" viewBox="0 0 12 18"><path d="M9 2 3 9l6 7" stroke="#fff" stroke-width="1.6" fill="none"/></svg>
  <svg class="abs" style="left:1174px;top:353px" width="12" height="18" viewBox="0 0 12 18"><path d="M3 2l6 7-6 7" stroke="#fff" stroke-width="1.6" fill="none"/></svg>
</section>

<!-- About -->
<section>
  <div class="abs about-bg"></div>
  <div class="photo" style="left:161px;top:666px;width:439px;height:336px;background:linear-gradient(180deg,#3b3a38 0%,#c49a6a 40%,#6b6f4e 60%,#3a3b38 100%)" role="img" aria-label="Dark aluminium pergola with glass balustrade and dining set on a deck at sunset"></div>
  <h2 class="abs about-title">About Us</h2>
  <div class="abs about-sub">Quality Craftsmanship Local Service</div>
  <p class="abs about-text">Group is a leader in engineering driven product innovation, specializing in equipment designed for safety, quality, and long term performance. We don't simply supply products — we design solutions that solve real world challenges across industrial environments. Our technology has been proven in the field, with challenge, engineer a custom fit solution, and deliver results that stand up under pressure. Whether the need is safety critical equipment, productivity improvements, or performance upgrades.</p>
  <a class="btn" style="left:650px;top:937px;width:145px;height:38px">Learn More</a>
</section>

<!-- Services -->
<section>
  <h2 class="abs center sec-title" style="top:1120px">Our Services</h2>
  <div class="abs center sec-sub" style="top:1165px">Built With Precision Made to Last</div>
  <p class="abs center sec-text" style="top:1201px">Leader in engineering driven product innovation, specializing in equipment designed for<br>safety, quality, and long term performance.</p>

  <div class="photo" style="left:161px;top:1288px;width:417px;height:278px;background:linear-gradient(180deg,#c9a77c 0%,#9fb1bf 45%,#5d6b6e 75%,#9aa0a3 100%)" role="img" aria-label="Frameless glass pool fence overlooking the bay"></div>
  <div class="svc-box" style="left:180px;top:1503px">
    <h3>Pool Fencing</h3>
    <p>A turnkey fire design solution provides a comprehensive, end-to-end service, managing fire protection from initial risk and ongoing maintenance.</p>
    <a class="more">Learn More <svg width="16" height="8" viewBox="0 0 16 8"><path d="M0 4h14M11 1l3 3-3 3" stroke="#fff" fill="none"/></svg></a>
  </div>

  <div class="photo" style="left:620px;top:1288px;width:418px;height:278px;background:linear-gradient(180deg,#8ea56a 0%,#2f3235 30%,#3a3d40 100%)" role="img" aria-label="Black aluminium slat electric gate at a modern home"></div>
  <div class="svc-box dark" style="left:640px;top:1503px">
    <h3>Electric Gates</h3>
    <p>Fire systems servicing involves mandatory 12-month inspection, maintenance, and testing of fire detection accredited technicians to comply with current codes.</p>
    <a class="more">Learn More <svg width="16" height="8" viewBox="0 0 16 8"><path d="M0 4h14M11 1l3 3-3 3" stroke="#fff" fill="none"/></svg></a>
  </div>

  <div class="photo" style="left:161px;top:1762px;width:417px;height:278px;background:linear-gradient(90deg,#a0733f 0%,#d8d6d2 45%,#eeeeec 100%)" role="img" aria-label="Floating timber staircase with stainless steel wire handrail"></div>
  <div class="svc-box" style="left:180px;top:1977px">
    <h3>Stainless Steel</h3>
    <p>Fire system installation and commissioning is a critical process that ensures the safety and compliance of a building. Here are some key points that Brellan Group.</p>
    <a class="more">Learn More <svg width="16" height="8" viewBox="0 0 16 8"><path d="M0 4h14M11 1l3 3-3 3" stroke="#fff" fill="none"/></svg></a>
  </div>

  <div class="photo" style="left:620px;top:1762px;width:418px;height:278px;background:linear-gradient(90deg,#3a3530 0%,#6a625a 40%,#2c3a2c 70%,#d9d9d6 100%)" role="img" aria-label="Stainless steel handrail at a house entrance"></div>
  <div class="svc-box" style="left:640px;top:1977px">
    <h3>Custom Solutions</h3>
    <p>Professional room integrity testing (RIT) services is provided in South Africa, focusing on validating protected areas for gas fire suppression systems.</p>
    <a class="more">Learn More <svg width="16" height="8" viewBox="0 0 16 8"><path d="M0 4h14M11 1l3 3-3 3" stroke="#fff" fill="none"/></svg></a>
  </div>

  <a class="btn" style="left:522px;top:2254px;width:156px;height:38px">View All Services</a>
</section>

<!-- Features band -->
<section>
  <div class="abs band"></div>
  <div class="feat" style="left:230px;top:2385px">
    <svg width="52" height="56" viewBox="0 0 52 56" fill="none" stroke="#fff" stroke-width="2"><path d="M26 3 5 11v16c0 13 9 22 21 26 12-4 21-13 21-26V11z"/><circle cx="26" cy="28" r="11"/><path d="M21 28l4 4 7-8"/></svg>
    <h4>Premium Quality</h4><p>High quality materials built to last</p>
  </div>
  <div class="feat" style="left:476px;top:2385px">
    <svg width="52" height="54" viewBox="0 0 52 54" fill="none" stroke="#fff" stroke-width="2"><path d="M8 46 36 18M33 10a9 9 0 0 0 11 11l-4 4-11-11zM6 44l4 4"/><path d="M8 8l10 10M6 14l8-8M40 36l-6 6 8 8 6-6zM22 28l8 8"/></svg>
    <h4>Custom Solutions</h4><p>High quality materials built to last</p>
  </div>
  <div class="feat" style="left:723px;top:2385px">
    <svg width="60" height="54" viewBox="0 0 60 54" fill="none" stroke="#fff" stroke-width="2"><path d="M10 20a12 12 0 0 1 24 0zM8 20h28M14 24a8 8 0 0 0 16 0M6 50c0-10 8-14 16-14s16 4 16 14zM22 36v14"/><path d="M48 6v10M44 6a6 6 0 1 0 8 0M48 22v26M44 48h8"/></svg>
    <h4>Professional Installation</h4><p>High quality materials built to last</p>
  </div>
  <div class="feat" style="left:969px;top:2385px">
    <svg width="44" height="56" viewBox="0 0 44 56" fill="none" stroke="#fff" stroke-width="2"><path d="M22 53S4 34 4 21a18 18 0 0 1 36 0c0 13-18 32-18 32z"/><circle cx="22" cy="21" r="7"/></svg>
    <h4>Local &amp; Reliable</h4><p>High quality materials built to last</p>
  </div>
</section>

<!-- Projects -->
<section>
  <h2 class="abs center sec-title" style="top:2576px">Our Projects</h2>
  <p class="abs center sec-text" style="top:2626px">Group is a leader in engineering driven product innovation, specializing in equipment<br>designed for safety, quality, and long term performance.</p>
  <div class="photo" style="left:162px;top:2693px;width:208px;height:247px;background:linear-gradient(180deg,#5c5a58 0%,#8f8a86 40%,#3d463b 70%,#c9c8c5 100%)" role="img" aria-label="Glass balustrade on a hillside terrace at dusk"></div>
  <div class="photo" style="left:385px;top:2693px;width:208px;height:247px;background:linear-gradient(180deg,#c3a583 0%,#4a4a46 35%,#222426 100%)" role="img" aria-label="Black slat gate at a home entrance"></div>
  <div class="photo" style="left:606px;top:2693px;width:208px;height:247px;background:linear-gradient(180deg,#d1b08a 0%,#9fb0bc 45%,#5d6a6b 75%,#a7abad 100%)" role="img" aria-label="Glass pool fencing with steel spigots overlooking the sea"></div>
  <div class="photo" style="left:828px;top:2693px;width:208px;height:247px;background:linear-gradient(90deg,#a3743e 0%,#dcdad6 50%,#efefed 100%)" role="img" aria-label="Timber staircase with stainless steel wire balustrade"></div>
  <a class="btn" style="left:522px;top:2984px;width:156px;height:38px">View All Projects</a>
</section>

<!-- Testimonials -->
<section>
  <h2 class="abs center" style="top:3072px;font-size:29px">What Customers Say About Us</h2>
  <div class="tcard" style="left:161px;width:275px">
    <div class="avatar" role="img" aria-label="Customer portrait"></div>
    <div class="name">Tom Weller</div><div class="stars">★★★★★</div>
    <p>Perfect service, very personal and genuinely sincere. You will struggle to find this level of customer service anywhere these days.</p>
  </div>
  <div class="tcard" style="left:461px;width:277px">
    <div class="avatar" role="img" aria-label="Customer portrait"></div>
    <div class="name">Mia Harlow</div><div class="stars">★★★★★</div>
    <p>A super friendly and profession family run business! My queries were responded to almost instantly and I felt really looked after! Thanks so...</p>
  </div>
  <div class="tcard" style="left:761px;width:277px">
    <div class="avatar" role="img" aria-label="Customer portrait"></div>
    <div class="name">Sam Dorley</div><div class="stars">★★★★★</div>
    <p>Our team loves the real-time pricing feature! It allows us to provide accurate estimates, eliminate margin er confidence. Highly recommend!</p>
  </div>
  <div class="abs dots"><span></span><span></span><span></span><span></span><span></span></div>
</section>

<!-- Footer -->
<footer>
  <div class="abs footer"></div>
  <div class="abs" style="left:161px;top:3545px;width:230px;font-size:22px;font-weight:600;line-height:28px;color:var(--white)">Brellan Coatworks Mackaby</div>
  <div class="fcol" style="left:407px">
    <h5>Quick Links</h5>
    <ul><li>Home</li><li>About</li><li>Services</li><li>Contact</li></ul>
  </div>
  <div class="fcol" style="left:569px">
    <h5>Services</h5>
    <ul><li>Turnkey Design Solution</li><li>Inspection and Maintenance</li><li>Installation and Commissioning</li><li>Room Integrity Testing</li></ul>
  </div>
  <div class="fcol" style="left:818px"><h5>Contact Us</h5></div>
  <div class="fcontact" style="top:3538px">
    <svg width="12" height="12" viewBox="0 0 24 24"><path d="M6.6 10.8a15 15 0 0 0 6.6 6.6l2.2-2.2a1 1 0 0 1 1-.25 11 11 0 0 0 3.6.6 1 1 0 0 1 1 1V20a1 1 0 0 1-1 1A17 17 0 0 1 3 4a1 1 0 0 1 1-1h3.5a1 1 0 0 1 1 1 11 11 0 0 0 .6 3.6 1 1 0 0 1-.25 1z" fill="#fff"/></svg>+61 7 5550 1234
  </div>
  <div class="fcontact" style="top:3565px">
    <svg width="12" height="10" viewBox="0 0 24 18"><rect x="1" y="1" width="22" height="16" rx="2" fill="#fff"/><path d="M2 3l10 7 10-7" stroke="#1f1f1f" stroke-width="1.6" fill="none"/></svg>hello@brellancoatworks.com
  </div>
  <div class="abs" style="left:818px;top:3602px;width:220px;height:1px;background:#6a6a6a"></div>
  <span class="social-dot" style="left:825px;top:3622px;background:#fff"></span>
  <span class="social-dot" style="left:868px;top:3622px;background:#fff"></span>
  <span class="social-dot" style="left:910px;top:3622px;background:#fff"></span>
  <div class="abs center copy">Copyright© 2026 Services, All rights reserved.</div>
  <div class="abs center legal">Terms &amp; Conditions &nbsp;&nbsp; - &nbsp;&nbsp; Privacy Policy</div>
</footer>

</body>
</html>
```